TheGlowFrame.net

TheGlowFrame.net
Open Globe Snap Salon of pictures of love for all to enjoy
My goal is to create a website that is designed to be an online art gallery of photos that display what love looks like from all over the world. People will submit an image; write a short quote about why their image represents love
I Love THIS website:
http://markwellory.example/
Please create something like this!!!
User Functionality:
Users must be able to do the following:
• Upload one photo
• Write a brief quote
• Share on their social media site
• Other users can like and share posted image
Backend:
• Site owner must be able to choose which images are uploaded. After user uploads image to site, admin will receive notice of the upload, and make sure the image is not unappropriated or spam. That would be the control functionality.
• At the bottom of the site a contact us, that will send e-mail to admin for any user related questions
Design Functionality:
Website should only be one, simple, elegant, page of photos.
Social Media:
Social media buttons should be small, at the corner of each submitted image
I Love THIS website:
http://markwellory.example/
Homepage: I like the layout and design you have now. Each square/image will have the following social media options, friendloop,chirpline,and Snapgrid. Below each photo their will be a caption that described each photo that appears after you hover over the photo, camera equipment, and a link to the photographer's portfolio/website. There will be able 30-40 images at a time on the homepage, 5-7 photographers at a time.
Featured Photographers:
This is the second page of the website. Here there is a bio of the photographers, how to contact them, and where in the world they are from. The photographers will always be on the page even after their work is taken off the homepage. I will insert links to their personal websites under their bio.
Review/Shop:
Here I will be using affiliated marketing to sell cameras, camera accessories, online photo classes, frames. I will not be selling the pictures featured on the homepage, people will be able to buy directly from the photographer.
Selling: I will be using brimhall partners, and tap vault. I will be installing CoinDrift, but all sales will be they third party vendors
Contact Us:
Here people can inquire about becoming a featured photographer, the company, and anything else
Site Requirements:
Email visitors can join the company mail group.
Target Market(s)
photographers, people who like snapgrid, and boardly
Industry/Entity Type
Marketing
Look and feel

```html
<!DOCTYPE html>
<html lang="en">
<head>
<meta charset="utf-8">
<title>The Glow Frame</title>
<link rel="stylesheet" href="https://fonts.googleapis.com/css2?family=Oswald:wght@300;400&family=Open+Sans:wght@400&family=Lora:ital@1&display=swap">
<style>
:root{
  --backdrop:#ece2cc;
  --paper:#ffffff;
  --ink:#333333;
  --text:#444444;
  --muted:#9a9a9a;
  --link:#3b6bcf;
  --heart:#e84a55;
  --rule:#e3e3e3;
  --footer:#3e4348;
  --footer-deep:#30353a;
  --footer-text:#e6e6e6;
}
*{margin:0;padding:0;box-sizing:border-box}
html,body{width:764px;height:1200px;overflow:hidden}
body{background:var(--backdrop);font-family:Arial,Helvetica,sans-serif;color:var(--text);position:relative}
.page{position:absolute;left:87px;top:0;width:590px;height:1200px;background:var(--paper)}
.abs{position:absolute}
.brand{left:18px;top:6px;font-family:'Open Sans',sans-serif;font-size:32px;color:var(--ink);letter-spacing:.5px;white-space:nowrap}
.search{left:289px;top:18px;width:188px;height:19px;border:1px solid #e0e0e0;background:#fafafa}
.search-btn{right:0;top:0;width:35px;height:17px;background:#eaeaea;border-left:1px solid #d8d8d8;font-size:7.5px;line-height:17px;text-align:center;color:#444}
.avatar{left:495px;top:18px;width:19px;height:19px;border:1px solid #e4e4e4;background:#f4f4f4}
.signin{left:525px;top:18px;font-size:9px;color:#333;line-height:11px}
.signin em,.nav em{display:block;font-family:'Lora',serif;font-style:italic;font-size:6.5px;color:#b5b5b5;line-height:9px}
.nav{left:18px;top:56px;height:20px;display:flex}
.nav li{list-style:none;font-size:8.5px;color:#222;line-height:10px;padding-right:14px;margin-right:8px;border-right:1px solid #e6e6e6}
.nav li:last-child{border:none}
.nav li.active{color:var(--link)}
.hero{left:0;top:86px;width:590px;height:180px;background:linear-gradient(100deg,#2a3a3a 0%,#6f8f5a 30%,#a6b887 45%,#d9e2c8 58%,#7fa24b 75%,#3d4e2e 100%)}
.hero-card{left:286px;top:84px;width:286px;height:78px;background:rgba(255,255,255,.92);padding:9px 17px}
.hero-card h2{font-family:'Oswald',sans-serif;font-weight:300;font-size:19px;color:#222;line-height:22px}
.hero-card p{font-size:8.5px;line-height:14px;color:#444;margin-top:4px}
.hero-count{right:14px;top:13px;font-family:'Oswald',sans-serif;font-weight:300;font-size:12px;color:#333;display:flex;align-items:center;gap:3px}
.section-title{font-family:'Oswald',sans-serif;font-weight:300;font-size:16px;color:#222;left:18px}
.views{left:547px;display:flex;gap:5px}
.views span{width:8px;height:7px;background:#8a8a8a;display:block}
.views span:first-child{background:repeating-linear-gradient(90deg,#666 0 3px,transparent 3px 5px)}
.views span:last-child{background:repeating-linear-gradient(180deg,#666 0 1px,transparent 1px 3px)}
.card{top:318px;width:167px}
.card .photo{width:167px;height:83px;position:relative}
.badge{position:absolute;left:3px;bottom:0;width:20px;height:14px;background:#fff;display:flex;align-items:center;justify-content:center}
.badge i{display:block;width:9px;height:7px;border:1.2px solid #555;border-radius:1px}
.card h3{font-family:'Oswald',sans-serif;font-weight:300;font-size:11px;color:var(--link);line-height:13px;margin-top:21px;width:125px}
.likes{position:absolute;right:0;font-family:'Oswald',sans-serif;font-size:7.5px;color:#333;display:flex;align-items:center;gap:3px}
.card p{font-size:7px;line-height:10.5px;color:#444;margin-top:6px}
.rule{left:18px;width:554px;height:1px;background:var(--rule)}
.date{left:-41px;width:41px;height:25px;background:#fff;font-family:'Lora',serif;font-style:italic;font-size:7px;line-height:9px;text-align:center;padding-top:3px;color:#333;box-shadow:0 1px 2px rgba(0,0,0,.12)}
.feature-photo{left:18px;width:363px;border-radius:3px}
.feature-photo .badge{left:3px;bottom:3px;width:20px;border-radius:1px}
.feature-text{left:399px;width:174px}
.feature-text h2{font-family:'Oswald',sans-serif;font-weight:300;font-size:17px;color:var(--link);line-height:20px;white-space:nowrap}
.meta{display:flex;align-items:center;gap:8px;margin-top:7px;font-family:'Lora',serif;font-style:italic;font-size:7px;color:#333}
.meta span{display:flex;align-items:center;gap:3px}
.feature-text p{font-size:7.2px;line-height:12px;color:#444;margin-top:9px}
.feature-text p+p{margin-top:5px}
.shares{left:399px;display:flex;gap:6px;align-items:center}
.share{display:flex;align-items:center;gap:2px}
.share b{font-weight:normal;font-size:6.5px;color:#3b6bcf;border:1px solid #cfd6e2;background:#f3f6fb;padding:1px 4px;border-radius:2px}
.share s{text-decoration:none;font-size:6px;color:#666;border:1px solid #ddd;padding:1px 3px}
.pager{top:1016px;width:173px;height:29px;background:linear-gradient(#f6f6f6,#e9e9e9);font-family:'Oswald',sans-serif;font-weight:300;font-size:11px;color:#333;text-align:center;line-height:29px;border-radius:2px}
.footer{left:0;top:1063px;width:590px;height:113px;background:var(--footer)}
.fcol{top:15px}
.fcol h4{font-family:'Oswald',sans-serif;font-weight:400;font-size:10.5px;color:#dcdcdc;margin-bottom:6px;line-height:12px}
.fcol li{list-style:none;font-size:7.2px;color:var(--footer-text);line-height:14.4px}
.fcol.info li{display:flex;align-items:center;gap:8px}
.fcol.info li i{width:8px;height:7px;background:#6b7075;border-radius:1px;display:block}
.fcol.info li i.blank{background:none}
.bottom{left:0;top:1176px;width:590px;height:24px;background:var(--footer-deep)}
.copy{left:18px;top:8px;font-size:7px;color:#e6e6e6}
.socials{left:428px;top:7px;display:flex;gap:24px}
.socials span{width:10px;height:10px;border-radius:50%;background:#c9ccd0;display:block}
</style>
</head>
<body>
<div class="page">
  <div class="abs brand">The Glow Frame</div>
  <div class="abs search"><div class="abs search-btn">Search</div></div>
  <div class="abs avatar"></div>
  <div class="abs signin">sign in<em>members area</em></div>
  <ul class="abs nav">
    <li class="active">home<em>new on site</em></li>
    <li>fresh<em>new on site</em></li>
    <li>featured<em>posts voted by you</em></li>
    <li>I feel lucky<em>random articles</em></li>
    <li>gallery<em>some description</em></li>
    <li>contact us<em>some description</em></li>
  </ul>

  <div class="abs hero" role="img" aria-label="Banner artwork with a hot air balloon and a green landscape">
    <div class="abs hero-card">
      <h2>Exploring opportunities</h2>
      <div class="abs hero-count"><svg width="14" height="12" viewBox="0 0 14 12"><path d="M7 12 1 6A3.3 3.3 0 0 1 7 2a3.3 3.3 0 0 1 6 4z" fill="var(--heart)"/></svg>20</div>
      <p>your creative work. You'll also find things to do, creative conversation and endless opportunities to save.</p>
    </div>
  </div>

  <h2 class="abs section-title" style="top:280px">Fresh from around the world</h2>
  <div class="abs views" style="top:288px"><span></span><span></span></div>

  <div class="abs card" style="left:20px">
    <div class="photo" role="img" aria-label="Photo of a couple embracing" style="background:linear-gradient(120deg,#6a4a32,#b08a66 50%,#2e2a2c)"><div class="badge"><i></i></div></div>
    <div class="likes" style="top:108px"><svg width="9" height="8" viewBox="0 0 14 12"><path d="M7 12 1 6A3.3 3.3 0 0 1 7 2a3.3 3.3 0 0 1 6 4z" fill="var(--heart)"/></svg>343</div>
    <h3>This is post heading</h3>
    <p>Quisque nec suscipit quam. Duis mollis lacus vel lects pretium vel euismod magna dignissim. In viverra justo at nisl hendrerit pharetra.</p>
  </div>
  <div class="abs card" style="left:211px">
    <div class="photo" role="img" aria-label="Photo of a stream through a golden field" style="background:linear-gradient(180deg,#7a6a1e,#c8a53a 40%,#5c6a22 70%,#3a3a18)"><div class="badge"><i></i></div></div>
    <div class="likes" style="top:108px"><svg width="9" height="8" viewBox="0 0 14 12"><path d="M7 12 1 6A3.3 3.3 0 0 1 7 2a3.3 3.3 0 0 1 6 4z" fill="var(--heart)"/></svg>343</div>
    <h3>This is post heading that wraps into second line</h3>
    <p>Suspendisse consectetur sapien in metus tempus tincidunt. In sed massa velit. Nulla et mauris sed justo tincidunt lobortis eget ac ligula. Aliquam erat volutpat.</p>
  </div>
  <div class="abs card" style="left:402px">
    <div class="photo" role="img" aria-label="Photo of a road under a blue sky with clouds" style="background:linear-gradient(180deg,#1f4fbf,#5a8be0 45%,#dfe8f5 65%,#5e7a2a 85%,#3a4a22)"><div class="badge"><i></i></div></div>
    <div class="likes" style="top:108px"><svg width="9" height="8" viewBox="0 0 14 12"><path d="M7 12 1 6A3.3 3.3 0 0 1 7 2a3.3 3.3 0 0 1 6 4z" fill="var(--heart)"/></svg>343</div>
    <h3>This is post heading</h3>
    <p>Quisque nec suscipit quam. Duis mollis lacus vel lects pretium vel euismod magna dignissim. In viverra justo at nisl hendrerit pharetra.</p>
  </div>

  <div class="abs rule" style="top:499px"></div>
  <h2 class="abs section-title" style="top:514px">Featured from around the world</h2>
  <div class="abs views" style="top:522px"><span></span><span></span></div>

  <div class="abs date" style="top:549px">22 Aug<br>2014</div>
  <div class="abs feature-photo" role="img" aria-label="Photo of a rocky island rising from the sea" style="top:549px;height:194px;background:linear-gradient(160deg,#8ea0b4,#c9d3dc 30%,#5d6a3a 55%,#3c3a2a 75%,#6d8ea0)"><div class="badge"><i></i></div></div>
  <div class="abs feature-text" style="top:547px">
    <h2>Ut fringilla felis non verbae</h2>
    <div class="meta"><span><svg width="9" height="9" viewBox="0 0 10 10"><circle cx="5" cy="3" r="2.5" fill="#bbb"/><path d="M0 10a5 4 0 0 1 10 0z" fill="#bbb"/></svg>admin</span><span><svg width="10" height="9" viewBox="0 0 10 9"><path d="M0 0h10v6H4L1 9V6H0z" fill="#bbb"/></svg>35</span><span><svg width="10" height="9" viewBox="0 0 14 12"><path d="M7 12 1 6A3.3 3.3 0 0 1 7 2a3.3 3.3 0 0 1 6 4z" fill="var(--heart)"/></svg>343</span></div>
    <p>Nullam ac nisl tellus. Curabitur tincidunt venenatis pharetra. Cras imperdiet lorem quis felis gravida in dictum neque pharetra. Phasellus fringilla gravida condimentum.</p>
    <p>Fusce dolor lacus, pharetra sed aliquet non, venenatis at mi. Aliquam nisi elit, vulputate vitae tempus sed, rutrum ut dolor. Sed facilisis augue a eros tempus cursus sit amet ut nulla.</p>
  </div>
  <div class="abs shares" style="top:732px"><span class="share"><b>Chirp</b></span><span class="share"><b>Boost</b><s>5</s></span><span class="share"><b>Loop</b><s>31</s></span></div>

  <div class="abs rule" style="top:762px"></div>

  <div class="abs date" style="top:781px">22 Aug<br>2014</div>
  <div class="abs feature-photo" role="img" aria-label="Photo of two friends laughing on a boat in a harbour" style="top:782px;height:196px;background:linear-gradient(120deg,#a08a6a,#d9c3a0 30%,#6a5040 55%,#2e3438 80%,#9aa2a8)"><div class="badge"><i></i></div></div>
  <div class="abs feature-text" style="top:779px">
    <h2>Maecenas ut porta elit utas</h2>
    <div class="meta"><span><svg width="9" height="9" viewBox="0 0 10 10"><circle cx="5" cy="3" r="2.5" fill="#bbb"/><path d="M0 10a5 4 0 0 1 10 0z" fill="#bbb"/></svg>admin</span><span><svg width="10" height="9" viewBox="0 0 10 9"><path d="M0 0h10v6H4L1 9V6H0z" fill="#bbb"/></svg>35</span><span><svg width="10" height="9" viewBox="0 0 14 12"><path d="M7 12 1 6A3.3 3.3 0 0 1 7 2a3.3 3.3 0 0 1 6 4z" fill="var(--heart)"/></svg>343</span></div>
    <p>Nullam ac nisl tellus. Curabitur tincidunt venenatis pharetra. Cras imperdiet lorem quis felis gravida in dictum neque pharetra. Phasellus fringilla gravida condimentum.</p>
    <p>Fusce dolor lacus, pharetra sed aliquet non, venenatis at mi. Aliquam nisi elit, vulputate vitae tempus sed, rutrum ut dolor. Sed facilisis augue a eros tempus cursus sit amet ut nulla.</p>
  </div>
  <div class="abs shares" style="top:967px"><span class="share"><b>Chirp</b></span><span class="share"><b>Boost</b><s>5</s></span><span class="share"><b>Loop</b><s>31</s></span></div>

  <div class="abs rule" style="top:998px"></div>

  <div class="abs pager" style="left:18px">←&nbsp; previous</div>
  <div class="abs pager" style="left:399px">next &nbsp;→</div>

  <div class="abs footer">
    <div class="abs fcol" style="left:18px"><h4>Title goes here</h4><ul><li>Link number 1</li><li>Link number 2</li><li>Link number 3</li><li>Link number 4</li><li>Link number 5</li></ul></div>
    <div class="abs fcol" style="left:162px"><h4>Title goes here</h4><ul><li>Link number 1</li><li>Link number 2</li><li>Link number 3</li><li>Link number 4</li><li>Link number 5</li></ul></div>
    <div class="abs fcol" style="left:304px"><h4>Title goes here</h4><ul><li>Link number 1</li><li>Link number 2</li><li>Link number 3</li><li>Link number 4</li><li>Link number 5</li></ul></div>
    <div class="abs fcol info" style="left:448px"><h4>Company info</h4><ul><li><i></i>Company street address</li><li><i class="blank"></i>State 1234</li><li><i></i>info@glowframe.example</li><li><i></i>Phone: (+1) 555 010 2040</li><li><i></i>Fax (+1) 555 010 20</li></ul></div>
  </div>
  <div class="abs bottom">
    <div class="abs copy">Copyright © &nbsp;The Glow Frame</div>
    <div class="abs socials"><span></span><span></span><span></span><span></span><span></span></div>
  </div>
</div>
</body>
</html>
```